TR Stationery - Modern Contemporary

Develop modern template for Letterhead and Stationery (business card, letterhead, envelopes) using the TR Logo and Icon

Colors
0054AA
0677BA
7BADD7
CADEEF
E8F1F8
00AB8E
00BBA5
67D7C9
C6EFE9
E9F9F6
EE7325
F08F49
F5BC92
FAE3D3
FDF4ED
6B429C
8869AF
B7A5CE
E3DAEB
F3F0F8

```html
<!DOCTYPE html>
<html lang="en">
<head>
<meta charset="utf-8">
<title>TR Stationery – Stationery Set</title>
<link href="https://fonts.googleapis.com/css2?family=Roboto:wght@400;500;700&family=Open+Sans:wght@400&display=swap" rel="stylesheet">
<style>
:root{
  --accent:#EE7325;
  --accent-soft:#F5BC92;
  --ink:#0054AA;
  --ink-mid:#0677BA;
  --ink-line:#7BADD7;
  --teal:#00AB8E;
  --purple:#6B429C;
  --paper:#ffffff;
  --bg:#E8F1F8;
  --text:#3f4650;
  --white:#ffffff;
}
*{margin:0;padding:0;box-sizing:border-box}
html,body{width:1200px;height:795px;overflow:hidden}
body{background:var(--bg);font-family:"Roboto",Arial,sans-serif;position:relative}
.piece{position:absolute;box-shadow:0 2px 6px rgba(0,40,90,.12)}
.brand{font-family:"Roboto",Arial,sans-serif;font-weight:700;line-height:1;white-space:nowrap;display:flex;align-items:center;gap:.3em}
.brand .dot{display:inline-block;width:.7em;height:.7em;background:var(--accent);flex:none}
.brand--dark{color:var(--ink)}
.brand--light{color:var(--white)}
.band{position:absolute;left:0;bottom:0;width:100%;display:block}

/* letterhead */
.letterhead{left:293px;top:99px;width:292px;height:415px;background:var(--paper)}
.letterhead .brand{position:absolute;left:31px;top:33px;font-size:9.5px}
.letterhead .sender{position:absolute;left:120px;top:33px;font-size:6.2px;line-height:8.3px;color:var(--text)}
.letterhead .sender .company{color:var(--accent);font-weight:500}
.letterhead .contacts{position:absolute;left:184px;top:32px;font-size:6.2px;line-height:8.3px;color:var(--text);list-style:none}
.letterhead .contacts li{display:flex;align-items:center;gap:2px}
.letterhead .contacts svg{width:6px;height:6px;flex:none}
.letter{position:absolute;left:31px;top:106px;width:231px;font-family:"Open Sans",Arial,sans-serif;font-size:5.1px;line-height:7.7px;color:var(--text);text-align:justify}
.letter p{margin-bottom:7.7px}
.signature{position:absolute;left:31px;top:306px;width:34px;height:30px;background:#eef3f8}

/* folder */
.folder{left:637px;top:80px;width:347px;height:437px;background:var(--ink)}
.folder .brand{position:absolute;left:0;right:0;top:226px;justify-content:center;font-size:30px}
.folder .url{position:absolute;left:0;right:0;top:400px;text-align:center;color:var(--white);font-size:9px;font-weight:500}
.folder .url span{color:var(--accent)}

/* business cards */
.card{left:187px;width:133px;height:75px;background:var(--ink)}
.card--front{top:551px}
.card--front .brand{position:absolute;left:0;right:0;top:32px;justify-content:center;font-size:10px}
.card--back{top:647px}
.card--back .brand{position:absolute;right:12px;top:14px;font-size:7px}
.card--back .person{position:absolute;left:12px;top:32px;font-size:4.2px;line-height:5px;color:var(--white)}
.card--back .person .name{color:var(--accent);font-weight:700}
.card--back .rule{position:absolute;left:12px;right:12px;top:45px;height:.5px;background:var(--ink-line)}
.card--back .contacts{position:absolute;left:12px;top:51px;font-size:3.7px;line-height:5px;color:var(--white);list-style:none}
.card--back .contacts li{display:flex;align-items:center;gap:1.5px}
.card--back .contacts svg{width:3.5px;height:3.5px}
.card--back .address{position:absolute;right:12px;top:51px;font-size:3.7px;line-height:5px;color:var(--white);text-align:right}

/* envelopes */
.envelope{top:561px;width:329px;height:157px;background:var(--paper)}
.envelope--front{left:353px}
.envelope--front .return{position:absolute;left:18px;top:28px;display:flex;flex-direction:column;align-items:center;gap:8px}
.envelope--front .brand{font-size:11px}
.envelope--front .address{text-align:center;font-size:6.6px;line-height:8px;color:var(--text)}
.envelope--back{left:713px}
.envelope--back .flap{position:absolute;left:0;top:0;width:329px;height:56px}
.envelope--back .brand{position:absolute;left:0;right:0;top:24px;justify-content:center;font-size:8px}
</style>
</head>
<body>

<section class="piece letterhead" aria-label="Letterhead">
  <div class="brand brand--dark"><span class="dot"></span>TR Stationery</div>
  <div class="sender">
    <div class="company">TR Stationery</div>
    <div>p.o box 40210</div>
    <div>reno, nv 89501</div>
  </div>
  <ul class="contacts">
    <li><svg viewBox="0 0 10 10"><path d="M2 1l2 2-1 1.3c.6 1.2 1.4 2 2.7 2.7L7 6l2 2-1.3 1.4C4.5 9 1 5.5.6 2.3z" fill="var(--accent)"/></svg>(555) 014-2200</li>
    <li><svg viewBox="0 0 10 10"><rect x="0.5" y="2" width="9" height="6" fill="var(--accent)"/><path d="M.5 2L5 5.5 9.5 2" stroke="#fff" fill="none" stroke-width=".8"/></svg>info@trstationery.com</li>
    <li><svg viewBox="0 0 10 10"><circle cx="5" cy="5" r="4" fill="none" stroke="var(--accent)" stroke-width="1.2"/><path d="M1 5h8M5 1c2 2 2 6 0 8M5 1c-2 2-2 6 0 8" stroke="var(--accent)" fill="none" stroke-width=".7"/></svg>www.trstationery.com</li>
  </ul>
  <div class="letter">
    <p>Dear customer,</p>
    <p>Lorem ipsum dolor sit amet, consectetur adipisicing elit, sed do eiusmod tempor incididunt ut labore et dolore magna aliqua. Ut enim ad minim veniam, quis nostrud exercitation ullamco laboris nisi ut aliquip ex ea commodo consequat. Duis aute irure dolor in reprehenderit in voluptate velit esse cillum dolore eu fugiat nulla pariatur. Excepteur sint occaecat cupidatat non proident, sunt in culpa qui officia deserunt mollit anim id est laborum.</p>
    <p>Lorem ipsum dolor sit amet, consectetur adipisicing elit, sed do eiusmod tempor incididunt ut labore et dolore magna aliqua. Ut enim ad minim veniam, quis nostrud exercitation ullamco laboris nisi ut aliquip ex ea commodo consequat. Duis aute irure dolor in reprehenderit in voluptate velit esse cillum dolore eu fugiat nulla pariatur. Excepteur sint occaecat cupidatat non proident, sunt in culpa qui officia deserunt mollit anim id est laborum.</p>
    <p>Lorem ipsum dolor sit amet, consectetur adipisicing elit, sed do eiusmod tempor incididunt ut labore et dolore magna aliqua. Ut enim ad minim veniam, quis nostrud exercitation ullamco laboris nisi ut aliquip ex ea commodo consequat. Duis aute irure dolor in reprehenderit in voluptate velit esse cillum dolore eu fugiat nulla pariatur. Excepteur sint occaecat cupidatat non proident, sunt in culpa qui officia deserunt mollit anim id est laborum.</p>
    <p>Lorem ipsum dolor sit amet, consectetur adipisicing elit, sed do eiusmod tempor incididunt ut labore et dolore magna aliqua. Ut enim ad minim veniam, quis nostrud exercitation ullamco laboris nisi ut aliquip ex ea commodo consequat. Duis aute irure dolor in reprehenderit.</p>
    <p>Yours Sincerely,</p>
  </div>
  <div class="signature" role="img" aria-label="Handwritten signature"></div>
  <svg class="band" viewBox="0 0 292 8" height="8" preserveAspectRatio="none">
    <rect width="292" height="8" fill="var(--ink)"/>
    <polygon points="0,0 205,0 198,8 0,8" fill="var(--accent)"/>
    <polygon points="205,0 207,0 200,8 198,8" fill="var(--white)"/>
  </svg>
</section>

<section class="piece folder" aria-label="Presentation folder">
  <div class="brand brand--light"><span class="dot"></span>TR Stationery</div>
  <div class="url">www.<span>trstationery</span>.com</div>
</section>

<section class="piece card card--front" aria-label="Business card front">
  <div class="brand brand--light"><span class="dot"></span>TR Stationery</div>
</section>

<section class="piece card card--back" aria-label="Business card back">
  <div class="brand brand--light"><span class="dot"></span>TR Stationery</div>
  <div class="person">
    <div class="name">DANIEL HARTWELL</div>
    <div>Managing Director</div>
  </div>
  <div class="rule"></div>
  <ul class="contacts">
    <li><svg viewBox="0 0 10 10"><circle cx="5" cy="5" r="4" fill="var(--accent)"/></svg>+15550142277</li>
    <li><svg viewBox="0 0 10 10"><rect x="0.5" y="2" width="9" height="6" fill="var(--accent)"/></svg>info@trstationery.com</li>
    <li><svg viewBox="0 0 10 10"><circle cx="5" cy="5" r="4" fill="none" stroke="var(--accent)" stroke-width="1.5"/></svg>www.trstationery.com</li>
  </ul>
  <div class="address">TR Stationery<br>14 Cedar Lane Drive<br>Oakville, ON L6J 1A1</div>
</section>

<section class="piece envelope envelope--front" aria-label="Envelope front">
  <div class="return">
    <div class="brand brand--dark"><span class="dot"></span>TR Stationery</div>
    <div class="address">p.o box 40210<br>reno, nv 89501</div>
  </div>
  <svg class="band" viewBox="0 0 329 8" height="8" preserveAspectRatio="none">
    <rect width="329" height="8" fill="var(--ink)"/>
    <polygon points="0,0 230,0 222,8 0,8" fill="var(--accent)"/>
    <polygon points="230,0 232,0 224,8 222,8" fill="var(--white)"/>
  </svg>
</section>

<section class="piece envelope envelope--back" aria-label="Envelope back">
  <svg class="flap" viewBox="0 0 329 56" preserveAspectRatio="none">
    <path d="M0 0H329L322 50Q321 55 315 55H14Q8 55 7 50Z" fill="var(--ink)"/>
  </svg>
  <div class="brand brand--light"><span class="dot"></span>TR Stationery</div>
</section>

</body>
</html>
```